Business Card Design

Business sales of reconditioned / used batteries with mobile delivery and install services. Customers base majority are auto car sales lots and individuals.

Card need to convey quality product reliability and quick prompt professional service.

Card must reflect excellence in customer care and product being offered

Target Market(s)

Auto car lots new and used. Auto repair shops. Individuals.

Industry/Entity Type

Business

Contact Information for Business Card

Cells Q-Dash
Cars, Trucks, Boats, Motorcycles, lawn mowers, power tools
Delivery & install available most vehicles
Mon-Sat 9-6pm
Lyle Brockett 501-738-2054
*product warranty 6 month shelf life battery/1 year blems battery

```html
<!DOCTYPE html>
<html lang="en">
<head>
<meta charset="UTF-8">
<title>Cells Q-Dash Business Card</title>
<link href="https://fonts.googleapis.com/css2?family=Lato:wght@400;700;900&display=swap" rel="stylesheet">
<style>
  :root {
    --backdrop: #6e6e6e;
    --card: #ffffff;
    --navy: #1d4580;
    --teal: #1c9bbf;
    --orange: #f07a2a;
    --white: #ffffff;
  }
  * { margin: 0; padding: 0; box-sizing: border-box; }
  html, body {
    width: 1200px;
    height: 900px;
    overflow: hidden;
    background: var(--backdrop);
    font-family: "Lato", sans-serif;
  }
  .card {
    position: absolute;
    left: 100px;
    top: 165px;
    width: 1000px;
    height: 570px;
    background: var(--card);
    overflow: hidden;
    box-shadow: 0 10px 30px rgba(0,0,0,0.35);
  }
  .card__band {
    position: absolute;
    left: 0;
    top: 0;
    width: 1000px;
    height: 570px;
  }
  .card__band path { fill: var(--navy); }
  .brand {
    position: absolute;
    top: 58px;
    width: 100%;
    text-align: center;
    font-size: 60px;
    font-weight: 700;
    color: var(--navy);
    letter-spacing: -0.5px;
  }
  .services {
    position: absolute;
    top: 146px;
    width: 100%;
    text-align: center;
    color: var(--orange);
    font-size: 29px;
    line-height: 1.3;
  }
  .services__line {
    display: inline-block;
    padding: 0 4px 3px;
    border-bottom: 1.5px solid var(--orange);
  }
  .services__hours { font-weight: 700; }
  .contact {
    position: absolute;
    top: 250px;
    width: 100%;
    text-align: center;
  }
  .contact__name {
    color: var(--navy);
    font-size: 42px;
    letter-spacing: 1px;
  }
  .contact__surname { font-weight: 700; }
  .contact__phone {
    margin-top: 8px;
    color: var(--teal);
    font-size: 28px;
    letter-spacing: 0.5px;
  }
  .contact__label { font-weight: 900; }
  .warranty {
    position: absolute;
    top: 450px;
    width: 100%;
    text-align: center;
    color: var(--white);
  }
  .warranty__title {
    font-size: 32px;
    font-weight: 900;
    letter-spacing: 0.5px;
  }
  .warranty__terms {
    margin-top: 10px;
    font-size: 24px;
    font-weight: 700;
    letter-spacing: 1px;
  }
</style>
</head>
<body>
  <div class="card">
    <svg class="card__band" viewBox="0 0 1000 570" aria-hidden="true">
      <path d="M0,455 Q560,350 1000,420 L1000,570 L0,570 Z"/>
    </svg>

    <h1 class="brand">Cells Q-Dash</h1>

    <p class="services">
      <span class="services__line">Trucks, Boats, Motorcycles, lawn mowers, power tools Delivery</span><br>
      <span class="services__line">&amp; install available most vehicles <span class="services__hours">Mon-Sat 9-6pm</span></span>
    </p>

    <div class="contact">
      <p class="contact__name">LYLE <span class="contact__surname">BROCKETT</span></p>
      <p class="contact__phone"><span class="contact__label">PHONE:</span> 501-738-2054</p>
    </div>

    <div class="warranty">
      <p class="warranty__title">PRODUCT WARRANTY</p>
      <p class="warranty__terms">6 MONTH SHELF LIFE BATTERY/1 YEAR BLEMS BATTERY</p>
    </div>
  </div>
</body>
</html>
```